Brisley Global Sourcing - we are Asian sourcing agents

We are sourcing agents based in the USA and we act as sourcing agents for clients in throughout the world. We focus primarily on custom sewn goods. So basically companies who do not have the in-house expertise to do it themselves, come to us and have us find suitable factories in Asia to do the production. We are middlemen. We find the factories...quote the project...manage the quality control and then deliver the goods directly to our customer's door. We pride ourselves in making the communication very easy and precise.

Current page is www.brisleysourcing.com

I am not happy w/ the overall look. The spacing...the photos, the fonts...the design elements...the pictures. I want a cool, crisp design that conveys professionalism and clearly depicts/explains what we do.

Coding

Coded - Design and coding required

Number of Pages Required

5+ page

Requirements
Must have
• use my logo....I like it...it was designed by someone on this website.
Nice to have
• a video/animation of the entire process would be wonderful. Showing initial contact with our office in the USA...then to my correspondence with my offices in Taiwan and in Hong Kong...and then back and fort w/ the customer.....and then between my people in Hong Kong/Taiwan with the local factories......and then a quote is generated and sent to my client......to samples being made and sent for approval.....to a PO being generated......to final samples being sent.....to the order being shipped and delivered to the clients warehouse. I was thinking of an animation showing arrows and text showing the back and forth communication and explaining how the process flows.

```html
<!DOCTYPE html>
<html lang="en">
<head>
<meta charset="utf-8">
<title>Brisley Global Sourcing</title>
<link href="https://fonts.googleapis.com/css2?family=Open+Sans:wght@600;700;800&display=swap" rel="stylesheet">
<style>
  :root {
    --navy: #1c2f6e;
    --nav-active: #1d5468;
    --nav-link: #e38b1c;
    --headline: #f6c544;
    --white: #ffffff;
    --cta: #c14a2e;
    --hero-deep: #14242b;
    --hero-mid: #2c4a55;
    --hero-light: #4f6b73;
  }
  * { margin: 0; padding: 0; box-sizing: border-box; }
  html, body { width: 1200px; height: 648px; overflow: hidden; }
  body { font-family: "Open Sans", Arial, sans-serif; background: var(--white); }

  .site-header {
    height: 58px;
    display: flex;
    align-items: center;
    justify-content: space-between;
    padding: 0 86px 0 100px;
    background: var(--white);
  }
  .brand {
    display: flex;
    align-items: center;
    gap: 8px;
    color: var(--navy);
    font-weight: 800;
    font-size: 15px;
    text-transform: uppercase;
    letter-spacing: 0.2px;
  }
  .brand-mark { width: 10px; height: 10px; background: var(--navy); }
  .main-nav { display: flex; gap: 22px; }
  .main-nav a {
    text-decoration: none;
    font-weight: 700;
    font-size: 13px;
    color: var(--nav-link);
    text-transform: uppercase;
  }
  .main-nav a.is-current { color: var(--nav-active); }

  .hero {
    position: relative;
    height: 590px;
    overflow: hidden;
  }
  .hero-photo {
    position: absolute; inset: 0;
    background:
      radial-gradient(ellipse 38% 55% at 55% 50%, rgba(70,110,140,0.55), transparent 70%),
      linear-gradient(180deg, var(--hero-light) 0%, var(--hero-mid) 40%, var(--hero-deep) 100%);
  }
  .hero-content {
    position: absolute;
    left: 169px;
    top: 150px;
    color: var(--white);
  }
  .hero-title {
    font-size: 43px;
    font-weight: 800;
    color: var(--headline);
    line-height: 1;
    margin-bottom: 22px;
  }
  .hero-lead {
    font-size: 15px;
    font-weight: 700;
    text-transform: uppercase;
    margin-bottom: 28px;
  }
  .cta-button {
    display: inline-block;
    background: var(--cta);
    color: var(--white);
    font-weight: 700;
    font-size: 16px;
    text-decoration: none;
    padding: 10px 18px;
    text-transform: uppercase;
    margin-bottom: 16px;
  }
  .contact-lines {
    list-style: none;
    font-size: 15px;
    font-weight: 700;
    line-height: 17px;
    text-transform: uppercase;
  }
  .slide-arrow {
    position: absolute;
    top: 368px;
    width: 18px;
    height: 28px;
  }
  .slide-arrow.prev { left: 137px; }
  .slide-arrow.next { left: 1044px; }
</style>
</head>
<body>
  <header class="site-header">
    <div class="brand"><span class="brand-mark"></span>Brisley Global Sourcing</div>
    <nav class="main-nav">
      <a class="is-current" href="#">Home</a>
      <a href="#">Product</a>
      <a href="#">Categories</a>
      <a href="#">Request Quote</a>
      <a href="#">Contact Us</a>
      <a href="#">About Us</a>
      <a href="#">Blog</a>
    </nav>
  </header>

  <section class="hero">
    <div class="hero-photo" role="img" aria-label="Two wooden rowing boats with blue interiors on dark calm water"></div>

    <div class="hero-content">
      <h1 class="hero-title">WELCOME TO</h1>
      <p class="hero-lead">Please contact us for immediate consultation regarding your outsourcing project.</p>
      <a class="cta-button" href="#">Request Quote &gt;&gt;</a>
      <ul class="contact-lines">
        <li>Tel: 555-014-2290</li>
        <li>Fax: 555-014-2291</li>
        <li>Email: info@brisleysourcing.com</li>
      </ul>
    </div>

    <svg class="slide-arrow prev" viewBox="0 0 18 28" aria-label="Previous slide">
      <polyline points="15,2 3,14 15,26" fill="none" stroke="#d8dde0" stroke-width="3"/>
    </svg>
    <svg class="slide-arrow next" viewBox="0 0 18 28" aria-label="Next slide">
      <polyline points="3,2 15,14 3,26" fill="none" stroke="#d8dde0" stroke-width="3"/>
    </svg>
  </section>
</body>
</html>
```